Killer business card for bowling event and marketing company

Rapid 'Q' Promotions is a sports marketing company that specializes in unique bowling events that provide return on investment for sponsors and memorable experiences for participants and spectators. We need a new business card that simultaneously communicates professionalism and fun. Our preferred colors are black and re

Target Market(s)

Executives in the marketing and sponsorship departments of companies, tourism executives, bowling center owners, and people who love to bowl.

Industry/Entity Type

Business

Contact Information for Business Card

Dean T Walsh
Rapid 'Q' Promotions
PO Box 47
Marlow Ridge, Kestrel USA 22871
Email: deant@rapidqpromotions.com
Mobile: 1-555-518-3762

Requirements
Must have
• Our preferred colors are black and red.
Nice to have
• I am considering the use of the attached image for the back of the card.

```html
<!DOCTYPE html>
<html lang="en">
<head>
<meta charset="utf-8">
<title>Rapid 'Q' Promotions – Business Card</title>
<link rel="stylesheet" href="https://fonts.googleapis.com/css2?family=Montserrat:wght@400;700&display=swap">
<style>
  :root {
    --backdrop: #7a868c;
    --card-black: #000000;
    --brand-red: #ee1a36;
    --red-mid: #d41430;
    --red-deep: #b80f27;
    --icon-red: #8e0f1d;
    --ink: #111111;
    --white: #ffffff;
  }
  * { margin: 0; padding: 0; box-sizing: border-box; }
  html, body {
    width: 1200px; height: 900px; overflow: hidden;
    background: var(--backdrop);
  }
  .card {
    position: absolute; left: 100px; top: 164px;
    width: 1000px; height: 572px;
    background: var(--card-black);
    overflow: hidden;
    box-shadow: 0 20px 40px rgba(0,0,0,.35);
  }
  .card__shapes { position: absolute; inset: 0; width: 100%; height: 100%; }
  .card__company {
    position: absolute; left: 48px; top: 44px;
    font-family: "Montserrat", sans-serif; font-weight: 700;
    font-size: 42px; color: var(--white);
  }
  .card__contact {
    position: absolute; right: 70px; top: 300px;
    text-align: right; color: var(--ink);
    font-family: "Montserrat", sans-serif;
  }
  .card__name { font-weight: 700; font-size: 30px; margin-bottom: 34px; margin-right: 8px; }
  .contact-line {
    display: flex; justify-content: flex-end; align-items: center; gap: 14px;
    font-size: 20px; line-height: 1.25; margin-bottom: 12px;
  }
  .contact-icon { flex: none; width: 34px; height: 34px; }
</style>
</head>
<body>
  <div class="card">
    <svg class="card__shapes" viewBox="0 0 1000 572" preserveAspectRatio="none" aria-hidden="true">
      <polygon points="0,520 400,210 960,100 960,572 0,572" fill="var(--brand-red)"/>
      <polygon points="0,520 400,210 120,572 0,572" fill="var(--red-mid)"/>
      <polygon points="0,520 400,210 230,430 80,572 0,572" fill="var(--red-deep)"/>
      <polygon points="0,520 400,210 300,280 0,560" fill="var(--red-mid)"/>
    </svg>

    <div class="card__company">Rapid 'Q' Promotions</div>

    <div class="card__contact">
      <div class="card__name">Dean T Walsh</div>
      <div class="contact-line">
        <span class="contact-text">1-555-518-3762</span>
        <svg class="contact-icon" viewBox="0 0 34 34" aria-label="Phone">
          <circle cx="17" cy="17" r="17" fill="var(--icon-red)"/>
          <path d="M12 10 l3 0 l1.5 4 l-2 1.5 a9 9 0 0 0 4 4 l1.5 -2 l4 1.5 l0 3 a2 2 0 0 1 -2 2 a14 14 0 0 1 -12 -12 a2 2 0 0 1 2 -2z" fill="var(--white)"/>
        </svg>
      </div>
      <div class="contact-line">
        <span class="contact-text">PO Box 47 Marlow Ridge,<br>Kestrel USA 22871</span>
        <svg class="contact-icon" viewBox="0 0 34 34" aria-label="Address">
          <circle cx="17" cy="17" r="17" fill="var(--icon-red)"/>
          <path d="M17 8 a6 6 0 0 1 6 6 c0 4.5 -6 11 -6 11 s-6 -6.5 -6 -11 a6 6 0 0 1 6 -6z" fill="var(--white)"/>
          <circle cx="17" cy="14" r="2.3" fill="var(--icon-red)"/>
        </svg>
      </div>
    </div>
  </div>
</body>
</html>
```